Harlow Ironworks Business Card

We need a business card design for a new small metal fabrication business in rural NSW, Australia.

The business (Harlow Ironworks) is owner operated by a man with the initials KB - much of the branding comes from this name.

Harlow Ironworks designs, engineers, repairs and manufactures a range of custom, quality metal works including vehicle trays, agricultural machinery impliments, trailers, wood splitters, fire pits, furniture etc.

The brand position focuses on custom work of the highest quality.

Business card design should show quality, attention to detail and stand out among a mass of business cards.

Logos are in the files

The grey color may be changed on the logo if required to stand out more.

There is an image attached of a simple card that is liked because it is clean, clear, simple, masculine and effective. It says 'quality'. As most of the work we do is custom it would be good to have the business card speak to this.

Target Market(s)

Rural and regional based Australians. Primarily adult male 25-60 yrs. Primary production / rural / travelling lifestyle.

Industry/Entity Type

Metal Fabrication

Contact Information for Business Card

The words 'custom quality fabrications' would be great somewhere perhaps on the backside (not on the information side)
Name
title
Phone: 0418 539 746 and (02) 6193 4827
email: info@harlowiw.com.au
www.harlowiw.com.au

address (2 lines)

Requirements
Nice to have
• Background colour should be very navy blue or black.
Should not have
• NO orange and blue combinations.
• Navy is OK

```html
<!DOCTYPE html>
<html lang="en">
<head>
<meta charset="utf-8">
<title>Harlow Ironworks Business Card</title>
<link href="https://fonts.googleapis.com/css2?family=Orbitron:wght@600&family=Open+Sans:wght@400;600&display=swap" rel="stylesheet">
<style>
  :root {
    --page: #e4e4e4;
    --navy: #111a36;
    --navy-deep: #0d1530;
    --card-grey: #c9c7c6;
    --steel: #8e8e8e;
    --steel-light: #9a9a9a;
    --green: #4bb33a;
    --white: #ffffff;
  }
  * { margin: 0; padding: 0; box-sizing: border-box; }
  html, body { width: 1200px; height: 1200px; overflow: hidden; }
  body { background: var(--page); position: relative; font-family: "Open Sans", sans-serif; }

  .card {
    position: absolute;
    left: 239px;
    width: 722px;
    height: 434px;
    box-shadow: 0 18px 30px rgba(0,0,0,0.25);
  }
  .card--front { top: 106px; background: linear-gradient(135deg, var(--navy) 0%, var(--navy-deep) 100%); }
  .card--back { top: 630px; background: var(--card-grey); }

  .brand-name {
    font-family: "Orbitron", sans-serif;
    font-weight: 600;
    color: var(--steel-light);
    letter-spacing: 0.04em;
    line-height: 1.1;
    text-transform: uppercase;
  }
  .card--front .brand-name { position: absolute; left: 56px; top: 34px; font-size: 24px; }

  .owner {
    position: absolute;
    right: 58px;
    top: 196px;
    text-align: right;
  }
  .owner__name {
    font-family: "Orbitron", sans-serif;
    font-weight: 600;
    color: var(--steel-light);
    font-size: 21px;
    letter-spacing: 0.06em;
    text-transform: uppercase;
  }
  .owner__title {
    font-family: "Orbitron", sans-serif;
    font-weight: 600;
    color: var(--green);
    font-size: 12px;
    letter-spacing: 0.5em;
    margin-top: 8px;
    margin-right: -0.5em;
    text-transform: uppercase;
  }

  .contact-list { position: absolute; left: 55px; top: 292px; list-style: none; }
  .contact-item { display: flex; align-items: flex-start; margin-bottom: 9px; }
  .contact-icon {
    width: 26px; height: 23px; border-radius: 3px; background: var(--white);
    display: flex; align-items: center; justify-content: center; flex-shrink: 0;
  }
  .contact-text { color: var(--white); font-size: 15px; line-height: 20px; margin-left: 20px; margin-top: 1px; }

  .address {
    position: absolute;
    right: 58px;
    bottom: 42px;
    text-align: right;
    color: var(--white);
    font-size: 15px;
    line-height: 20px;
  }

  .back-lockup {
    position: absolute; left: 0; right: 0; top: 104px;
    display: flex; flex-direction: column; align-items: center;
  }
  .back-mark { width: 64px; height: 64px; background: var(--green); margin-bottom: 26px; }
  .card--back .brand-name { font-size: 28px; color: var(--steel); text-align: center; }
  .tagline {
    margin-top: 26px;
    text-align: center;
    font-family: "Orbitron", sans-serif;
    font-weight: 600;
    text-transform: uppercase;
  }
  .tagline__top { color: var(--steel); font-size: 15px; letter-spacing: 0.08em; }
  .tagline__bottom { color: var(--green); font-size: 11px; letter-spacing: 0.7em; margin-top: 6px; margin-right: -0.7em; }
</style>
</head>
<body>
  <section class="card card--front">
    <div class="brand-name">Harlow<br>Ironworks</div>

    <div class="owner">
      <div class="owner__name">Kieran Blake</div>
      <div class="owner__title">Owner / Fabricator</div>
    </div>

    <ul class="contact-list">
      <li class="contact-item">
        <span class="contact-icon">
          <svg width="16" height="11" viewBox="0 0 16 11"><rect x="0.5" y="0.5" width="15" height="10" fill="none" stroke="#111a36"/><path d="M0.5 0.5 L8 6 L15.5 0.5" fill="none" stroke="#111a36"/></svg>
        </span>
        <span class="contact-text">info@harlowiw.com.au</span>
      </li>
      <li class="contact-item">
        <span class="contact-icon">
          <svg width="15" height="15" viewBox="0 0 16 16"><circle cx="8" cy="8" r="7" fill="none" stroke="#111a36"/><ellipse cx="8" cy="8" rx="3" ry="7" fill="none" stroke="#111a36"/><path d="M1 8 H15 M2 4.5 H14 M2 11.5 H14" stroke="#111a36"/></svg>
        </span>
        <span class="contact-text">www.harlowiw.com.au</span>
      </li>
      <li class="contact-item">
        <span class="contact-icon">
          <svg width="16" height="13" viewBox="0 0 16 13"><path d="M1 4 Q8 -1 15 4 L13 5.5 L11 4 L5 4 L3 5.5 Z" fill="#111a36"/><rect x="2.5" y="6" width="11" height="6" rx="1" fill="#111a36"/><circle cx="8" cy="9" r="1.6" fill="#fff"/></svg>
        </span>
        <span class="contact-text">0418 539 746<br>(02) 6193 4827</span>
      </li>
    </ul>

    <address class="address" style="font-style: normal;">14 Foundry Lane<br>Weldon Creek NSW 2652</address>
  </section>

  <section class="card card--back">
    <div class="back-lockup">
      <div class="back-mark"></div>
      <div class="brand-name">Harlow<br>Ironworks</div>
      <div class="tagline">
        <div class="tagline__top">Custom Quality</div>
        <div class="tagline__bottom">Fabrications</div>
      </div>
    </div>
  </section>
</body>
</html>
```